New Meal Prep Flyer for New Package Deals

We are looking for a design that displays our new packages that we offer. If you take a look at our website www.brambleforkmeals.com, and click on packages , you'll see the way we display them currently . We would like something similar to that in style . The first package is called "Horizon" and this package will be a 1 week package (7 days ), 2 meals a day, for a price of $195.00. The second package is called "Amber" and this package will be a 3 week package (21 days) 2 meals per day, for a price of $546.00 , the third package is a 6 week+ package (45 days), and it is called "Evergreen" , 2 meals per day , and the price is $1080.00 .
For the Amber Package , can you put next to it "Save $42.00!"
For the Evergreen Package, can you put next to it "Save $180!"
We also want our logo on the flyer (see attached), and we are just looking for a 1 page flyer , 8 1/2 x 11.

```html
<!DOCTYPE html>
<html lang="en">
<head>
<meta charset="utf-8">
<title>Bramblefork Meal Prep Packages Flyer</title>
<link rel="stylesheet" href="https://fonts.googleapis.com/css2?family=Montserrat:wght@500;600;700;800&family=Roboto:wght@500;700&display=swap">
<style>
  :root {
    --page-bg: #ececec;
    --paper: #ffffff;
    --brand-grey: #8c8c8c;
    --ink-dark: #3a3a3a;
    --green: #7aae1e;
    --green-top: #6c9f1a;
    --green-bottom: #a5cb3b;
    --orange-top: #ea7510;
    --orange-bottom: #f6b421;
    --orange-text: #e8730f;
    --grey-top: #777777;
    --grey-bottom: #9b9b9b;
    --card-rim: #e2e2e2;
    --band: #f4f4f6;
    --gold: 196, 160, 84;
    --leaf: 122, 181, 29;
  }
  * { box-sizing: border-box; margin: 0; padding: 0; }
  html, body { width: 704px; height: 1200px; overflow: hidden; background: var(--page-bg); }
  body { position: relative; font-family: "Montserrat", sans-serif; }

  .flyer {
    position: absolute; left: 0; top: 144px;
    width: 704px; height: 911px;
    background: var(--paper);
    overflow: hidden;
  }

  .brand-name {
    position: absolute; left: 0; right: 0; top: 48px;
    text-align: center;
    font-family: "Montserrat", sans-serif;
    font-weight: 600; font-size: 71px; line-height: 86px;
    letter-spacing: 1px;
    color: var(--brand-grey);
  }
  .tagline {
    position: absolute; left: 0; right: 0; top: 140px;
    text-align: center;
    font-family: "Roboto", sans-serif; font-weight: 700;
    font-size: 37px; line-height: 42px;
    color: var(--green); letter-spacing: -0.5px;
  }
  .tagline .divider { display: inline-block; margin: 0 14px; font-weight: 500; }

  .sparkle-field {
    position: absolute; left: 0; top: 212px; width: 704px; height: 540px;
    background:
      linear-gradient(90deg,
        rgba(var(--gold),0.38) 0%, rgba(var(--gold),0.16) 7%, rgba(var(--gold),0.08) 50%,
        rgba(var(--gold),0.16) 93%, rgba(var(--gold),0.38) 100%);
    -webkit-mask-image: linear-gradient(180deg, transparent 0%, #000 8%, #000 88%, transparent 100%);
            mask-image: linear-gradient(180deg, transparent 0%, #000 8%, #000 88%, transparent 100%);
  }

  .package {
    position: absolute; top: 220px; width: 198px; height: 494px;
    color: #fff; text-align: center;
    border: 4px solid var(--card-rim);
    box-shadow: 0 2px 6px rgba(0,0,0,0.12);
  }
  .package--horizon { left: 43px; background: linear-gradient(180deg, var(--green-top), var(--green-bottom)); border-radius: 44px 14px 72px 14px; }
  .package--amber { left: 255px; background: linear-gradient(180deg, var(--orange-top), var(--orange-bottom)); border-radius: 44px 14px 14px 14px; }
  .package--evergreen { left: 468px; background: linear-gradient(180deg, var(--grey-top), var(--grey-bottom)); border-radius: 14px 44px 14px 72px; }

  .package__tier {
    position: absolute; left: 18px; right: 18px; top: 26px; height: 34px;
    background: #fff; border-radius: 6px;
    font-weight: 800; font-size: 20px; line-height: 34px; letter-spacing: 0.5px;
    box-shadow: 0 2px 3px rgba(0,0,0,0.15);
  }
  .package--horizon .package__tier { color: var(--green); }
  .package--amber .package__tier { color: var(--orange-text); }
  .package--evergreen .package__tier { color: var(--ink-dark); }

  .package__weeks { position: absolute; left: 0; right: 0; top: 62px; font-weight: 700; font-size: 70px; line-height: 76px; }
  .package__label { position: absolute; left: 0; right: 0; top: 142px; font-weight: 800; font-size: 31px; line-height: 32px; letter-spacing: -0.3px; }
  .package__days { position: absolute; left: 20px; right: 20px; top: 210px; font-weight: 500; font-size: 19px; line-height: 24px; display: flex; align-items: center; gap: 6px; }
  .package__days::before, .package__days::after { content: ""; flex: 1; height: 1.5px; background: rgba(255,255,255,0.85); }

  .package__meals {
    position: absolute; left: 22px; right: 22px; top: 252px; height: 77px;
    border: 1.5px dashed rgba(255,255,255,0.8); border-radius: 4px;
    font-weight: 700; font-size: 25px; line-height: 26px; padding-top: 11px; letter-spacing: 0.5px;
  }

  .package__price-tab {
    position: absolute; left: 46px; right: 46px; top: 351px; height: 28px;
    background: #5a5a5a; border-radius: 4px 4px 0 0;
    font-weight: 500; font-size: 19px; line-height: 30px; color: #fff; z-index: 2;
  }
  .package__price {
    position: absolute; left: 14px; right: 14px; top: 360px; height: 64px;
    background: #fff; border-radius: 10px;
    font-weight: 800; font-size: 34px; line-height: 72px; letter-spacing: -0.8px;
    white-space: nowrap;
  }
  .package--evergreen .package__price { font-size: 31px; letter-spacing: -1px; }
  .package__price sup { font-size: 16px; vertical-align: top; position: relative; top: -10px; margin-right: 1px; }
  .package--horizon .package__price { color: var(--green); }
  .package--amber .package__price { color: var(--orange-text); }
  .package--evergreen .package__price { color: var(--ink-dark); }

  .savings-badge { position: absolute; width: 96px; height: 96px; z-index: 3; }
  .savings-badge--amber { left: 313px; top: 657px; }
  .savings-badge--evergreen { left: 526px; top: 653px; }
  .savings-badge svg { position: absolute; inset: 0; }
  .savings-badge__text {
    position: absolute; inset: 0; display: flex; flex-direction: column; justify-content: center; align-items: center;
    color: #fff; transform: rotate(-16deg); font-weight: 600; white-space: nowrap;
  }
  .savings-badge__word { font-size: 17px; line-height: 19px; letter-spacing: 1px; }
  .savings-badge__amount { font-size: 18px; line-height: 21px; font-weight: 700; }
  .savings-badge__amount sup { font-size: 10px; }

  .leaf-sprig {
    position: absolute; width: 112px; height: 40px; z-index: 4;
    background: radial-gradient(ellipse at 50% 55%, rgba(var(--leaf),0.85) 0%, rgba(var(--leaf),0.55) 45%, rgba(var(--leaf),0) 72%);
  }
  .leaf-sprig--amber { left: 320px; top: 736px; }
  .leaf-sprig--evergreen { left: 534px; top: 733px; }

  .footer-band { position: absolute; left: 0; top: 758px; width: 704px; height: 153px; background: var(--band); }
  .footer-band__texture {
    position: absolute; right: 0; top: 0; width: 360px; height: 153px;
    background: radial-gradient(ellipse at 85% 60%, rgba(200,200,205,0.55), rgba(244,244,246,0) 70%);
  }
  .footer-pitch {
    position: absolute; left: 44px; top: 770px;
    font-weight: 800; font-size: 25px; line-height: 29px; color: var(--green);
  }
  .footer-cta {
    position: absolute; left: 44px; top: 872px;
    font-weight: 500; font-size: 17.5px; line-height: 22px; color: #2a2a2a;
  }
  .footer-url {
    position: absolute; left: 372px; top: 850px; width: 332px; height: 35px;
    background: var(--green); border-radius: 6px 0 0 6px;
    color: #fff; font-weight: 500; font-size: 20px; line-height: 35px; padding-left: 16px;
    white-space: nowrap;
  }
</style>
</head>
<body>
  <main class="flyer">
    <h1 class="brand-name">BRAMBLEFORK</h1>
    <p class="tagline">HEALTHY KITCHEN<span class="divider">|</span>MEAL PREP</p>

    <div class="sparkle-field" role="img" aria-label="Scattered gold star confetti behind the packages"></div>

    <section class="package package--horizon">
      <div class="package__tier">HORIZON</div>
      <div class="package__weeks">1</div>
      <div class="package__label">WEEK<br>PACKAGE</div>
      <div class="package__days">(7 DAYS)</div>
      <div class="package__meals">2 MEALS<br>A DAY</div>
      <div class="package__price-tab">PRICE</div>
      <div class="package__price"><sup>$</sup>195.00</div>
    </section>

    <section class="package package--amber">
      <div class="package__tier">AMBER</div>
      <div class="package__weeks">3</div>
      <div class="package__label">WEEK<br>PACKAGE</div>
      <div class="package__days">(21 DAYS)</div>
      <div class="package__meals">2 MEALS<br>A DAY</div>
      <div class="package__price-tab">PRICE</div>
      <div class="package__price"><sup>$</sup>546.00</div>
    </section>

    <section class="package package--evergreen">
      <div class="package__tier">EVERGREEN</div>
      <div class="package__weeks">6</div>
      <div class="package__label">WEEK<br>PACKAGE</div>
      <div class="package__days">(45 DAYS)</div>
      <div class="package__meals">2 MEALS<br>A DAY</div>
      <div class="package__price-tab">PRICE</div>
      <div class="package__price"><sup>$</sup>1080.00</div>
    </section>

    <div class="footer-band">
      <div class="footer-band__texture" role="img" aria-label="Soft halftone dot wave texture"></div>
    </div>

    <div class="savings-badge savings-badge--amber">
      <svg viewBox="0 0 96 96" aria-hidden="true">
        <rect x="16" y="16" width="64" height="64" rx="8" fill="#3a3a3a"/>
        <rect x="16" y="16" width="64" height="64" rx="8" fill="#3a3a3a" transform="rotate(45 48 48)"/>
        <rect x="16" y="16" width="64" height="64" rx="8" fill="#3a3a3a" transform="rotate(22.5 48 48)"/>
      </svg>
      <div class="savings-badge__text">
        <span class="savings-badge__word">SAVE</span>
        <span class="savings-badge__amount"><sup>$</sup>42.00!</span>
      </div>
    </div>

    <div class="savings-badge savings-badge--evergreen">
      <svg viewBox="0 0 96 96" aria-hidden="true">
        <rect x="16" y="16" width="64" height="64" rx="8" fill="#3a3a3a"/>
        <rect x="16" y="16" width="64" height="64" rx="8" fill="#3a3a3a" transform="rotate(45 48 48)"/>
        <rect x="16" y="16" width="64" height="64" rx="8" fill="#3a3a3a" transform="rotate(22.5 48 48)"/>
      </svg>
      <div class="savings-badge__text">
        <span class="savings-badge__word">SAVE</span>
        <span class="savings-badge__amount"><sup>$</sup>180.00!</span>
      </div>
    </div>

    <div class="leaf-sprig leaf-sprig--amber" role="img" aria-label="Pair of green leaves under the savings badge"></div>
    <div class="leaf-sprig leaf-sprig--evergreen" role="img" aria-label="Pair of green leaves under the savings badge"></div>

    <p class="footer-pitch">Use the value of<br>your package toward<br>take out or meal prep!</p>
    <p class="footer-cta">Start earning your rewards now!</p>
    <div class="footer-url">www.brambleforkmeals.com</div>
  </main>
</body>
</html>
```